Dental Lab Delivery Box Design 163x115x97mm

* AI file of the box attached
* Full-Color outside and one color inside
* Return pictures of the 3D design; so we can have a better idea of how it will turn out
* Match Logo Color and Design
* Please find attached Words doc for the wording
* Research the dental lab delivery
* Attached our sister lab dental lab design
*
Updates

Thank for designing! We are reviewing and asking designers for improvements. We have extended the due date! More designs welcome!

Target Market(s)

Dental Office

Industry/Entity Type

Dental Lab

Font styles to use
Serif

Colors
0054AA
0677BA
7BADD7
CADEEF
E8F1F8

Requirements
Must have
• Advance, Clean, and Matched Logo color
Nice to have
• Graphics
Should not have
• Too much words or over advertise

```html
<!DOCTYPE html>
<html lang="en">
<head>
<meta charset="utf-8">
<title>Nerva Dental Inc – Delivery Box Dieline</title>
<link rel="stylesheet" href="https://fonts.googleapis.com/css2?family=Jost:wght@400;500&display=swap">
<style>
  :root{
    --navy:#0054AA;
    --blue:#0677BA;
    --sky:#7BADD7;
    --mist:#CADEEF;
    --ice:#E8F1F8;
    --page:#BBCCE2;
    --white:#FFFFFF;
    --cut:#C77BC9;
  }
  html,body{margin:0;padding:0;width:1200px;height:1200px;overflow:hidden;background:var(--page);}
  .canvas{width:1200px;height:1200px;display:flex;align-items:center;justify-content:center;}
  .dieline{width:1140px;height:1140px;display:block;}
  .flap{fill:var(--blue);stroke:var(--cut);stroke-width:1;}
  .panel-white{fill:var(--white);stroke:var(--cut);stroke-width:1;}
  .brand{font-family:"Jost",sans-serif;font-weight:500;fill:var(--navy);}
  .brand-name{font-size:40px;letter-spacing:1px;}
  .brand-sub{font-size:11px;letter-spacing:4px;}
  .tagline{font-family:"Jost",sans-serif;font-weight:400;font-size:11px;fill:var(--blue);}
  .tagline-light{fill:var(--white);}
  .body-copy{font-family:"Jost",sans-serif;font-weight:400;font-size:6.4px;fill:#33415a;}
  .mark-dot{fill:var(--sky);}
</style>
</head>
<body>
<main class="canvas">
<svg class="dieline" viewBox="10 20 1080 1000" xmlns="http://www.w3.org/2000/svg" aria-label="Nerva Dental Inc delivery box dieline">
  <defs>
    <radialGradient id="wave-glow" cx="50%" cy="50%" r="62%">
      <stop offset="0" stop-color="#FFFFFF"/>
      <stop offset="0.55" stop-color="#FFFFFF"/>
      <stop offset="0.72" stop-color="#CADEEF"/>
      <stop offset="0.86" stop-color="#7BADD7"/>
      <stop offset="1" stop-color="#0054AA"/>
    </radialGradient>
    <linearGradient id="stripe-fade" x1="0" y1="0" x2="0" y2="1">
      <stop offset="0" stop-color="#0054AA"/>
      <stop offset="0.5" stop-color="#FFFFFF"/>
      <stop offset="1" stop-color="#0054AA"/>
    </linearGradient>
    <linearGradient id="band-fade" x1="0" y1="0" x2="1" y2="0">
      <stop offset="0" stop-color="#FFFFFF"/>
      <stop offset="1" stop-color="#0054AA"/>
    </linearGradient>
  </defs>

  <!-- top tuck flap -->
  <path class="flap" d="M302 55 H798 V205 L765 222 H335 L302 205 Z"/>

  <!-- lid row -->
  <path class="flap" d="M37 232 H217 V432 H37 V375 H31 V290 H37 Z"/>
  <rect class="panel-white" x="217" y="227" width="176" height="210"/>
  <rect x="393" y="227" width="314" height="210" fill="url(#wave-glow)" role="img" aria-label="Flowing blue wave graphic around a white centre"/>
  <rect class="panel-white" x="707" y="227" width="175" height="210"/>
  <path class="flap" d="M882 232 H1062 V290 H1069 V375 H1062 V432 H882 Z"/>

  <g class="logo logo-lid">
    <circle class="mark-dot" cx="492" cy="322" r="12"/>
    <text class="brand brand-name" x="512" y="343">NERVA</text>
    <text class="brand brand-sub" x="514" y="358">DENTAL INC</text>
    <text class="tagline" x="550" y="381" text-anchor="middle">Every Detail Matters</text>
  </g>

  <g class="logo logo-side-left" transform="translate(305 332) rotate(-90)">
    <text class="brand" x="0" y="0" font-size="26" text-anchor="middle">NERVA</text>
    <text class="brand" x="0" y="12" font-size="7" letter-spacing="2.5" text-anchor="middle">DENTAL INC</text>
  </g>
  <g class="logo logo-side-right" transform="translate(795 332) rotate(90)">
    <text class="brand" x="0" y="0" font-size="26" text-anchor="middle">NERVA</text>
    <text class="brand" x="0" y="12" font-size="7" letter-spacing="2.5" text-anchor="middle">DENTAL INC</text>
  </g>

  <!-- back row -->
  <path class="panel-white" d="M300 452 L340 440 H397 V610 H300 Z"/>
  <rect class="panel-white" x="397" y="437" width="306" height="173"/>
  <rect x="634" y="437" width="50" height="173" fill="url(#stripe-fade)"/>
  <path class="panel-white" d="M703 440 H760 L799 452 V610 H703 Z"/>

  <g class="back-copy" transform="translate(1034 1047) rotate(180)">
    <text class="body-copy" x="417" y="500">Welcome to Nerva! Headquartered in Riverton Bay, we</text>
    <text class="body-copy" x="417" y="509">are a full digital dental lab for all you need. We strive to build</text>
    <text class="body-copy" x="417" y="518">excellent relationships and services with our clients, utilize highly</text>
    <text class="body-copy" x="417" y="527">experienced technicians and advanced case management systems.</text>
    <text class="body-copy" x="417" y="536">Nerva stands for quality, care and service. We care for your</text>
    <text class="body-copy" x="417" y="545">team as one team.</text>
    <text class="body-copy" x="417" y="560">Nerva looks forward to building and improving your reputation and</text>
    <text class="body-copy" x="417" y="569">bringing more smiles to our services.</text>
  </g>
  <g class="logo logo-back" transform="translate(659 572) rotate(180)">
    <text class="brand" x="0" y="0" font-size="14" text-anchor="middle">NERVA</text>
    <text class="brand" x="0" y="7" font-size="4.5" letter-spacing="1.5" text-anchor="middle">DENTAL INC</text>
  </g>

  <!-- base row -->
  <path class="flap" d="M403 614 H262 Q228 622 228 665 V752 Q230 780 262 790 L403 826 Z"/>
  <rect x="403" y="612" width="294" height="214" fill="url(#wave-glow)" role="img" aria-label="Flowing blue wave graphic around a white centre"/>
  <path class="flap" d="M697 614 H838 Q872 622 872 665 V752 Q870 780 838 790 L697 826 Z"/>

  <g class="logo logo-base">
    <circle class="mark-dot" cx="506" cy="704" r="11"/>
    <text class="brand brand-name" x="524" y="724" font-size="36">NERVA</text>
    <text class="brand brand-sub" x="524" y="738">DENTAL INC</text>
    <text class="tagline" x="550" y="774" text-anchor="middle">Every Detail Matters</text>
  </g>

  <!-- front row -->
  <path class="flap" d="M397 836 H265 Q232 840 232 872 Q242 962 322 1000 H397 Z"/>
  <rect class="panel-white" x="397" y="826" width="306" height="174"/>
  <path class="flap" d="M703 836 H835 Q868 840 868 872 Q858 962 778 1000 H703 Z"/>
  <rect x="497" y="970" width="206" height="17" fill="url(#band-fade)"/>
  <text class="tagline tagline-light" x="624" y="982" text-anchor="middle" font-size="10">Every Detail Matters</text>
  <g class="logo logo-front">
    <text class="brand" x="437" y="982" font-size="16">NERVA</text>
    <text class="brand" x="440" y="989" font-size="4.5" letter-spacing="1.5">DENTAL INC</text>
  </g>
</svg>
</main>
</body>
</html>
```